Meridian Rest Supply Needs Business Card

Looking for a very nice looking business card. Creative but not extravagant. We sell beds and pillows across the U.S. and need something professional but catchy. I have attached the logo.

Name : Dale Fenwick
Title : President
Phone : (800) 417-2964
Email: sleep@quorvana.com
Website: www.quorvana.com

Can be single-sided or double-sided
horizontal or vertical

Can use Blues/Greys

Target Market(s)

Mass Market

Industry/Entity Type

Retail

Contact Information for Business Card

Name : Dale Fenwick
Title : President
Phone : (800) 417-2964
Email: sleep@quorvana.com
Website: www.quorvana.com

Requirements
Must have
• Clean, Modern, Smooth
• Can use Blues/Greys
• On the other side without the information - have something simple like www.quorvana.com or our logo
Nice to have
• Surprise me
Should not have
• Nothing crazy, nothing cluttered

```html
<!DOCTYPE html>
<html lang="en">
<head>
<meta charset="utf-8">
<title>Quorvana Business Card</title>
<link rel="stylesheet" href="https://fonts.googleapis.com/css2?family=Source+Sans+3:wght@400;600&display=swap">
<style>
  :root {
    --backdrop: #e4e6e8;
    --card: #f6f7f8;
    --card-edge: #e1e4e6;
    --brand-blue: #2ea0da;
    --ink: #222629;
  }
  * { box-sizing: border-box; margin: 0; padding: 0; }
  html, body {
    width: 1200px;
    height: 900px;
    overflow: hidden;
    background: var(--backdrop);
    font-family: "Source Sans 3", sans-serif;
  }
  .business-card {
    position: absolute;
    left: 150px;
    top: 172px;
    width: 900px;
    height: 555px;
    background: var(--card);
    border: 1px solid var(--card-edge);
    border-radius: 24px;
    box-shadow: 0 18px 40px rgba(0, 0, 0, 0.12);
  }
  .brand {
    position: absolute;
    right: 58px;
    top: 92px;
    display: flex;
    align-items: center;
    gap: 18px;
  }
  .brand-dot {
    width: 34px;
    height: 34px;
    border-radius: 50%;
    background: var(--brand-blue);
  }
  .brand-name {
    font-weight: 600;
    font-size: 64px;
    line-height: 1;
    color: var(--brand-blue);
  }
  .holder {
    position: absolute;
    left: 47px;
    top: 268px;
  }
  .holder-name {
    font-weight: 600;
    font-size: 34px;
    line-height: 1.1;
    color: var(--brand-blue);
  }
  .holder-title {
    font-weight: 400;
    font-size: 26px;
    line-height: 1.15;
    color: var(--ink);
  }
  .divider {
    position: absolute;
    left: 0;
    right: 0;
    top: 354px;
    height: 3px;
    background: var(--brand-blue);
  }
  .contact-list {
    position: absolute;
    right: 56px;
    top: 386px;
    list-style: none;
    text-align: right;
  }
  .contact-item {
    display: flex;
    justify-content: flex-end;
    align-items: center;
    gap: 14px;
    font-size: 23px;
    line-height: 38px;
    color: var(--ink);
  }
  .contact-icon {
    width: 18px;
    height: 18px;
    fill: var(--brand-blue);
    flex: none;
  }
</style>
</head>
<body>
  <main class="business-card">
    <div class="brand">
      <span class="brand-dot"></span>
      <span class="brand-name">quorvana</span>
    </div>

    <div class="holder">
      <p class="holder-name">Dale Fenwick</p>
      <p class="holder-title">President</p>
    </div>

    <div class="divider"></div>

    <ul class="contact-list">
      <li class="contact-item">
        <span>(800) 417-2964</span>
        <svg class="contact-icon" viewBox="0 0 24 24" aria-hidden="true">
          <path d="M6.6 10.8a15.1 15.1 0 0 0 6.6 6.6l2.2-2.2a1 1 0 0 1 1-.25 11.4 11.4 0 0 0 3.6.57 1 1 0 0 1 1 1V20a1 1 0 0 1-1 1A17 17 0 0 1 3 4a1 1 0 0 1 1-1h3.5a1 1 0 0 1 1 1c0 1.25.2 2.45.57 3.57a1 1 0 0 1-.25 1z"/>
        </svg>
      </li>
      <li class="contact-item">
        <span>sleep@quorvana.com</span>
        <svg class="contact-icon" viewBox="0 0 24 24" aria-hidden="true">
          <path d="M2 5h20v14H2z M3.5 6.5 12 13l8.5-6.5" fill="var(--brand-blue)" stroke="#f6f7f8" stroke-width="1.5"/>
        </svg>
      </li>
      <li class="contact-item">
        <span>www.quorvana.com</span>
        <svg class="contact-icon" viewBox="0 0 24 24" aria-hidden="true">
          <circle cx="12" cy="12" r="10"/>
          <path d="M7 7c2 0 3 1 3 2.5S8.5 12 9.5 13.5 12 15 11 18M14 5c-.5 1.5 1 2.5 2.5 2.5S19 9 18 11.5s-2.5 1-3 3" fill="none" stroke="#f6f7f8" stroke-width="1.6"/>
        </svg>
      </li>
    </ul>
  </main>
</body>
</html>
```